wedding invitation card

Requirement:
1. White background, pink elements on the card, simple elegant looking
2. content:
Please join us as we celebrate new beginnings, new dreams,
and most importantly, new love at the marriage of
Miss Lin Qiao and Mr. Haoran Mu
Friday, The First of January
Two Thousand Fifteen at Eleven o’clock
Coral Tide Resort Palm Breeze Garden.

Reception will be followed at Lotus Hall at Half-Past Twelve o'clock

Please RSVP before December 18th 2015 by email: qiaolin0815@mailvexa.com

3. Flat paper
4. be able to change the size of the design according to printing requirement

Industry/Entity Type

Wedding

```html
<!DOCTYPE html>
<html lang="en">
<head>
<meta charset="utf-8">
<title>Wedding Invitation – Lin Qiao &amp; Haoran Mu</title>
<link rel="stylesheet" href="https://fonts.googleapis.com/css2?family=Pinyon+Script&family=Great+Vibes&family=Arimo&display=swap">
<style>
  :root {
    --backdrop: #cbced4;
    --paper: #ffffff;
    --paper-edge: #9a9ca2;
    --ornament-pink: #ec6aad;
    --ornament-soft: #f7c3de;
    --text-pink: #e2499c;
    --accent-pink: #e01b8c;
  }
  * { box-sizing: border-box; margin: 0; padding: 0; }
  html, body {
    width: 1200px;
    height: 900px;
    overflow: hidden;
    background: var(--backdrop);
  }
  .canvas {
    position: relative;
    width: 1200px;
    height: 900px;
  }
  .invitation-card {
    position: absolute;
    left: 140px;
    top: 130px;
    width: 928px;
    height: 625px;
    background: var(--paper);
    border: 1px solid var(--paper-edge);
  }
  .corner-flourish {
    position: absolute;
    width: 180px;
    height: 140px;
  }
  .corner-flourish--top-left { left: 4px; top: 4px; background: radial-gradient(ellipse at 0 0, var(--ornament-pink) 0%, var(--ornament-soft) 50%, transparent 72%); }
  .corner-flourish--top-right { right: 4px; top: 4px; background: radial-gradient(ellipse at 100% 0, var(--ornament-pink) 0%, var(--ornament-soft) 50%, transparent 72%); }
  .corner-flourish--bottom-left { left: 4px; bottom: 4px; background: radial-gradient(ellipse at 0 100%, var(--ornament-pink) 0%, var(--ornament-soft) 50%, transparent 72%); }
  .corner-flourish--bottom-right { right: 4px; bottom: 4px; background: radial-gradient(ellipse at 100% 100%, var(--ornament-pink) 0%, var(--ornament-soft) 50%, transparent 72%); }
  .monogram-crest {
    position: absolute;
    left: 393px;
    top: 42px;
    width: 142px;
    height: 158px;
    border-radius: 50% 50% 46% 46%;
    background: radial-gradient(circle at 50% 50%, var(--paper) 38%, var(--ornament-soft) 60%, var(--ornament-pink) 100%);
  }
  .invitation-line {
    position: absolute;
    left: 0;
    width: 100%;
    height: 40px;
    line-height: 40px;
    text-align: center;
    white-space: nowrap;
    color: var(--text-pink);
    font-family: "Pinyon Script", cursive;
    font-size: 22px;
  }
  .invitation-line--names { font-size: 30px; }
  .invitation-line--date {
    font-family: "Great Vibes", cursive;
    color: var(--accent-pink);
    font-size: 26px;
    font-weight: 700;
  }
  .invitation-line--venue { font-size: 25px; }
  .invitation-line--address {
    font-family: "Arimo", sans-serif;
    font-size: 18px;
  }
  .invitation-line--rsvp { font-size: 19px; }
</style>
</head>
<body>
<main class="canvas">
  <article class="invitation-card">
    <div class="corner-flourish corner-flourish--top-left" role="img" aria-label="Pink floral scroll flourish in the corner"></div>
    <div class="corner-flourish corner-flourish--top-right" role="img" aria-label="Pink floral scroll flourish in the corner"></div>
    <div class="corner-flourish corner-flourish--bottom-left" role="img" aria-label="Pink floral scroll flourish in the corner"></div>
    <div class="corner-flourish corner-flourish--bottom-right" role="img" aria-label="Pink floral scroll flourish in the corner"></div>

    <div class="monogram-crest" role="img" aria-label="Pink crowned monogram crest with the couple's names and a heart"></div>

    <p class="invitation-line" style="top:212px">Please join us as we celebrate new beginnings, new dreams,</p>
    <p class="invitation-line" style="top:254px">and most importantly, new love at the marriage of</p>
    <p class="invitation-line invitation-line--names" style="top:298px">Miss Lin Qiao and Mr. Haoran Mu</p>
    <p class="invitation-line invitation-line--date" style="top:344px">On Friday, the First of January, Two Thousand Fifteen</p>
    <p class="invitation-line invitation-line--date" style="top:386px">At Eleven O'Clock in the Morning</p>
    <p class="invitation-line invitation-line--venue" style="top:428px">Coral Tide Resort Palm Breeze Garden</p>
    <p class="invitation-line invitation-line--address" style="top:468px">418 Seabreeze Ave. Honolulu, Hawaii, 96815</p>
    <p class="invitation-line" style="top:506px">Reception to follow at Lotus Hall at Half-Past Twelve O'Clock</p>
    <p class="invitation-line invitation-line--rsvp" style="top:548px">Please RSVP to qiaolin0815@mailvexa.com before December 18th, 2015</p>
  </article>
</main>
</body>
</html>
```